Gutschein-Design für Tätowierer
Zielgruppe
Ich bin ein Tätowierer und suche ein hochwertiges Design, meine Zielgruppe sind Leute jeden Alters
Aufgabenstellung
-Farbe auf meiner Karte sollte wie bei meiner Webseite www.brenno-tattoo.de sein Pazifikblau/ Marineblau
-Es soll schlicht sein
-mein Logo soll auf die Vorderseite mittig (in schwarz)
-ein Rand soll enthalten sein in einem blauton
-auf die Rückseite sollen Felder zum ausfüllen sein wie zum Beispiel Name, Gutschein wert usw..
-Maße ca. 21 x 10,5 cm

```html
<!DOCTYPE html>
<html lang="de">
<head>
<meta charset="utf-8">
<title>Gutschein – Brenno Ink</title>
<link rel="stylesheet" href="https://fonts.googleapis.com/css2?family=Barlow:wght@500;600;700&family=Caveat+Brush&family=Kaushan+Script&display=swap">
<style>
  :root {
    --stage: #2b2624;
    --card: #1f1b1a;
    --card-edge: #171413;
    --ink-white: #f4f2f0;
    --field: #ffffff;
    --field-text: #2a2625;
    --pacific: #3fa4d6;
    --navy: #1f6e9e;
    --photo-dark: #1d1a19;
    --photo-mid: #4a4543;
    --photo-light: #8c8785;
  }
  * { box-sizing: border-box; margin: 0; padding: 0; }
  html, body {
    width: 1200px; height: 800px; overflow: hidden;
    background: var(--stage);
    font-family: "Barlow", Arial, sans-serif;
  }
  .canvas {
    position: relative; width: 1200px; height: 800px;
  }
  .card {
    position: absolute; left: 250px; width: 700px; height: 350px;
    background: var(--card);
    overflow: hidden;
    box-shadow: 0 18px 40px rgba(0,0,0,.45);
  }
  .card--front { top: 35px; }
  .card--back { top: 415px; }

  /* Front */
  .front-photo {
    position: absolute; top: 0; right: 0; width: 420px; height: 100%;
    background:
      linear-gradient(90deg, var(--card) 0%, rgba(31,27,26,.6) 30%, rgba(31,27,26,0) 60%),
      radial-gradient(ellipse at 65% 45%, var(--photo-light) 0%, var(--photo-mid) 40%, var(--photo-dark) 85%);
  }
  .brand {
    position: absolute; top: 26px; right: 34px;
    display: flex; align-items: center; gap: 10px;
    color: var(--ink-white);
    font-weight: 700; font-size: 22px; letter-spacing: .5px;
  }
  .brand__dot {
    width: 34px; height: 34px; border-radius: 50%;
    border: 3px solid var(--ink-white);
  }
  .headline {
    position: absolute; left: 70px; top: 105px;
    color: var(--ink-white);
  }
  .headline__title {
    font-family: "Caveat Brush", cursive;
    font-size: 124px; line-height: 1;
  }
  .headline__value {
    display: flex; align-items: baseline; gap: 14px;
    margin-left: 70px; margin-top: -6px;
  }
  .headline__label {
    font-family: "Kaushan Script", cursive;
    font-size: 34px;
  }
  .headline__amount {
    font-family: "Barlow", sans-serif;
    font-weight: 700; font-size: 58px;
    background: linear-gradient(180deg, var(--pacific), var(--navy));
    -webkit-background-clip: text; background-clip: text;
    color: transparent;
  }

  /* Back */
  .back-photo {
    position: absolute; top: 0; left: 0; width: 300px; height: 100%;
    background:
      linear-gradient(90deg, rgba(0,0,0,0) 60%, var(--card) 100%),
      linear-gradient(110deg, #d9d6d4 0%, #9e9a98 35%, #5b5654 60%, #2c2827 100%);
  }
  .back-info {
    position: absolute; top: 24px; left: 320px; right: 28px;
  }
  .contacts {
    display: flex; gap: 34px; margin-bottom: 16px;
    color: var(--ink-white); font-weight: 600; font-size: 17px;
  }
  .contact { display: flex; align-items: center; gap: 8px; }
  .contact svg { width: 20px; height: 20px; }
  .field {
    display: flex; align-items: center;
    height: 54px; margin-bottom: 14px; padding-left: 24px;
    background: var(--field);
    color: var(--field-text);
    font-weight: 700; font-size: 19px;
  }
  .note {
    margin-top: 10px;
    color: var(--ink-white);
    font-weight: 500; font-size: 12.5px; line-height: 1.4;
    text-align: center;
  }
</style>
</head>
<body>
<main class="canvas">
  <section class="card card--front">
    <div class="front-photo" role="img" aria-label="Schwarzweißfoto: Tätowierer mit Handschuhen bei der Arbeit"></div>
    <div class="brand"><span class="brand__dot"></span>Brenno Ink</div>
    <div class="headline">
      <div class="headline__title">Gutschein</div>
      <div class="headline__value">
        <span class="headline__label">Im wert von</span>
        <span class="headline__amount">30€</span>
      </div>
    </div>
  </section>

  <section class="card card--back">
    <div class="back-photo" role="img" aria-label="Schwarzweißfoto: Vorlage und fertiges Tattoo einer Madonnenskulptur"></div>
    <div class="back-info">
      <div class="contacts">
        <span class="contact">
          <svg viewBox="0 0 20 20"><circle cx="10" cy="10" r="8" fill="none" stroke="var(--pacific)" stroke-width="2"/></svg>
          brenno_ink
        </span>
        <span class="contact">
          <svg viewBox="0 0 20 20" fill="none" stroke="var(--pacific)" stroke-width="1.6">
            <circle cx="10" cy="10" r="8"/>
            <ellipse cx="10" cy="10" rx="3.5" ry="8"/>
            <line x1="2" y1="10" x2="18" y2="10"/>
          </svg>
          www.brenno-tattoo.de
        </span>
      </div>
      <div class="field">Betrag :</div>
      <div class="field">Gültig Bis :</div>
      <div class="field">Code :</div>
      <p class="note">Lorem ipsum dolor sit amet, consectetur adipiscing elit, sed do eiusmod tempor incididunt ut labore et dolore magna aliqua. Ut enim ad minim veniam, quis nostrud exercitation ullamco.</p>
    </div>
  </section>
</main>
</body>
</html>
```